Flyer Design

I need a flyer as Iam starting a business which cleans Leather couches,sofas,chairs for residential and businesses.
We clean the interiors of automobiles and marine craft, boats large and small.
We would like to be able to get across the message that we are affordable, personal and reliable.
The Gold coast is our market and within this area there is a large amount of holiday apartments and houses which do experience high traffic to their living and dinning areas.

Target Market(s)

Target market Home,Apartment,Marine and Auto Owners

Industry/Entity Type

Residential

Requirements
Must have
• The flyer must have Company name which is PURE HIDE RESTORE MOBILE NUMBER
0431759204
EMAIL tramkell@vornexmail.com
Colours would like bright Gold or green or Red eith black lettering very modern font
Nice to have
• I would like to keep it as simple and clean looking.but eye catching
Should not have
• Dont want the flyer to look like a Real Estate flyer or a pizza advertisement.

```html
<!DOCTYPE html>
<html lang="en">
<head>
<meta charset="utf-8">
<title>Pure Hide Restore — Flyer Variants</title>
<link rel="stylesheet" href="https://fonts.googleapis.com/css2?family=Yanone+Kaffeesatz:wght@400;500&family=Fjalla+One&family=Oswald:wght@300;400&display=swap">
<style>
  :root {
    --bronze: #6b5a36;
    --crimson: #8e2726;
    --ink: #231f20;
    --paper: #ffffff;
    --gold-label: #8a7447;
    --gold-label-warm: #b08f5c;
  }
  html, body {
    margin: 0;
    padding: 0;
    overflow: hidden;
    background: var(--paper);
  }
  .sheet {
    position: relative;
    width: 1200px;
    height: 490px;
    background: var(--paper);
    overflow: hidden;
  }
  .flyer {
    position: absolute;
    top: 0;
    width: 380px;
    height: 490px;
    background: var(--paper);
    overflow: hidden;
  }
  .flyer--dark { left: 0; }
  .flyer--red { left: 412px; }
  .flyer--stacked { left: 820px; }

  .brand {
    position: absolute;
    z-index: 2;
    margin: 0;
    font-family: "Yanone Kaffeesatz", sans-serif;
    font-weight: 500;
    line-height: 0.9;
    letter-spacing: 0.5px;
    color: var(--bronze);
  }
  .flyer--dark .brand,
  .flyer--red .brand {
    top: 30px;
    left: 0;
    width: 100%;
    text-align: center;
    font-size: 82px;
  }
  .flyer--red .brand { color: var(--crimson); }
  .flyer--stacked .brand {
    top: 22px;
    left: 24px;
    font-size: 84px;
    line-height: 0.92;
  }

  .tagline {
    position: absolute;
    margin: 0;
    font-family: "Fjalla One", sans-serif;
    font-size: 17px;
    line-height: 29px;
    color: var(--ink);
  }
  .flyer--dark .tagline,
  .flyer--red .tagline {
    top: 198px;
    left: 0;
    width: 100%;
    text-align: center;
  }
  .flyer--red .tagline { color: var(--bronze); }
  .flyer--stacked .tagline {
    top: 288px;
    left: 30px;
  }

  .couch-art {
    position: absolute;
    z-index: 1;
    background: var(--ink);
    border-radius: 40px 40px 6px 6px;
  }
  .flyer--dark .couch-art,
  .flyer--red .couch-art {
    left: 18px;
    top: 268px;
    width: 344px;
    height: 104px;
  }
  .flyer--red .couch-art { background: var(--crimson); }
  .flyer--stacked .couch-art {
    left: 180px;
    top: 22px;
    width: 200px;
    height: 136px;
    border-radius: 30px 0 6px 30px;
  }

  .contact-band {
    position: absolute;
    left: 0;
    width: 100%;
    background: var(--ink);
    color: var(--paper);
    text-align: center;
    font-family: "Oswald", sans-serif;
  }
  .flyer--dark .contact-band { top: 372px; height: 118px; }
  .flyer--red .contact-band { top: 370px; height: 108px; background: var(--crimson); }
  .flyer--stacked .contact-band { top: 362px; height: 128px; }

  .base-stripe {
    position: absolute;
    left: 0;
    top: 478px;
    width: 100%;
    height: 12px;
    background: var(--bronze);
  }

  .contact-heading {
    margin: 16px 0 0;
    font-size: 10px;
    font-weight: 400;
  }
  .flyer--red .contact-heading { margin-top: 10px; }
  .contact-line {
    margin: 4px 0 0;
    white-space: nowrap;
  }
  .contact-label {
    font-size: 13px;
    font-weight: 300;
    color: var(--gold-label);
    text-transform: uppercase;
    margin-right: 4px;
  }
  .flyer--red .contact-label { color: var(--gold-label-warm); }
  .contact-value--phone {
    font-size: 27px;
    font-weight: 400;
    letter-spacing: 0.5px;
    line-height: 32px;
  }
  .contact-value--email {
    font-size: 14px;
    font-weight: 300;
  }
</style>
</head>
<body>
<main class="sheet">

  <article class="flyer flyer--dark">
    <h1 class="brand">pure hide<br>restore</h1>
    <p class="tagline">We clean leather couches, sofas,chairs<br>for residential and businesses.</p>
    <div class="couch-art" role="img" aria-label="Silhouette illustration of a two-seat leather sofa"></div>
    <section class="contact-band">
      <p class="contact-heading">Contact us:</p>
      <p class="contact-line"><span class="contact-label">Mobile number</span><span class="contact-value--phone">0431759204</span></p>
      <p class="contact-line"><span class="contact-label">Email</span><span class="contact-value--email">tramkell@vornexmail.com</span></p>
    </section>
  </article>

  <article class="flyer flyer--red">
    <h1 class="brand">pure hide<br>restore</h1>
    <p class="tagline">We clean leather couches, sofas,chairs<br>for residential and businesses.</p>
    <div class="couch-art" role="img" aria-label="Silhouette illustration of a two-seat leather sofa in red"></div>
    <section class="contact-band">
      <p class="contact-heading">Contact us:</p>
      <p class="contact-line"><span class="contact-label">Mobile number</span><span class="contact-value--phone">0431759204</span></p>
      <p class="contact-line"><span class="contact-label">Email</span><span class="contact-value--email">tramkell@vornexmail.com</span></p>
    </section>
    <div class="base-stripe"></div>
  </article>

  <article class="flyer flyer--stacked">
    <h1 class="brand">pure<br>hide<br>restore</h1>
    <div class="couch-art" role="img" aria-label="Cropped silhouette illustration of a leather sofa"></div>
    <p class="tagline">We clean leather couches, sofas,chairs<br>for residential and businesses.</p>
    <section class="contact-band">
      <p class="contact-heading">Contact us:</p>
      <p class="contact-line"><span class="contact-label">Mobile number</span><span class="contact-value--phone">0431759204</span></p>
      <p class="contact-line"><span class="contact-label">Email</span><span class="contact-value--email">tramkell@vornexmail.com</span></p>
    </section>
  </article>

</main>
</body>
</html>
```